Need FaceBook, Linkedin, Instagram, Twitter banners designed

We need to have the logos ovantri wallet logo, and the TallyBloom a service of ovantri Logo. Both attached herein. turned into Social Media Banners. (FaceBook, LinkedIn, Instagram, Twitter). Different Banners for each of the two logos for each of the 4 media outlets:
1) ovantri - Just the wallet
2) TallyBloom

```html
<!DOCTYPE html>
<html lang="en">
<head>
<meta charset="utf-8">
<title>ovantri – Social Media Banners</title>
<link rel="stylesheet" href="https://fonts.googleapis.com/css2?family=Montserrat:wght@400;500;600;700&display=swap">
<style>
  :root {
    --canvas: #585d5c;
    --shadow: #464a4f;
    --orange: #f08249;
    --sky: #83d3f5;
    --cyan: #00b5dd;
    --plum: #621463;
    --ink: #57504f;
    --paper: #ffffff;
    --mist: #e3e3e3;
  }
  * { margin: 0; padding: 0; box-sizing: border-box; }
  html, body { width: 1029px; height: 1200px; overflow: hidden; }
  body {
    position: relative;
    background: var(--canvas);
    font-family: "Montserrat", Arial, sans-serif;
  }
  .banner {
    position: absolute;
    display: block;
    box-shadow: 13px 13px 0 var(--shadow);
  }
  .banner--facebook { left: 203px; top: 42px; width: 525px; height: 231px; }
  .banner--linkedin { left: 203px; top: 357px; width: 608px; height: 185px; }
  .banner--twitter  { left: 203px; top: 626px; width: 605px; height: 202px; }
  .banner--post     { top: 902px; width: 201px; height: 201px; box-shadow: 12px 12px 0 var(--shadow); }
  .banner--post-1 { left: 203px; }
  .banner--post-2 { left: 414px; }
  .banner--post-3 { left: 625px; }

  .format-label {
    position: absolute;
    left: 214px;
    color: var(--paper);
    font-size: 28px;
    font-weight: 500;
    line-height: 1;
    letter-spacing: 0.5px;
  }
  .format-label--facebook  { top: 300px; }
  .format-label--linkedin  { top: 569px; }
  .format-label--twitter   { top: 845px; }
  .format-label--instagram { top: 1126px; }

  .brand-name { font-family: "Montserrat", Arial, sans-serif; font-weight: 600; fill: var(--ink); }
  .brand-dot { fill: var(--cyan); }
  .join-bar { fill: var(--ink); }
  .join-label { font-family: "Montserrat", Arial, sans-serif; font-weight: 600; fill: var(--paper); }
  .handle { font-family: "Montserrat", Arial, sans-serif; font-weight: 400; }
  .website { font-family: "Montserrat", Arial, sans-serif; font-weight: 400; fill: var(--ink); }
  .website--light { fill: var(--paper); font-weight: 500; }
</style>
</head>
<body>

  <!-- Facebook cover -->
  <svg class="banner banner--facebook" viewBox="0 0 907 398" aria-label="Facebook banner">
    <rect width="907" height="398" fill="var(--orange)"/>
    <polygon points="254,0 756,0 653,398 150,398" fill="var(--sky)"/>
    <polygon points="254,0 150,398 101,398" fill="var(--plum)"/>
    <polygon points="756,0 807,0 653,398" fill="var(--plum)"/>
    <g class="brand-lockup">
      <text class="brand-name" x="442" y="187" font-size="64" text-anchor="middle">ovantri</text>
      <circle class="brand-dot" cx="572" cy="166" r="10"/>
    </g>
    <polygon class="join-bar" points="229,313 483,313 477,340 218,340"/>
    <text class="join-label" x="241" y="333" font-size="16">JOIN US</text>
    <text class="handle" x="318" y="330" font-size="10" fill="var(--sky)">@companyaccount</text>
    <text class="website" x="495" y="330" font-size="10">www.companywebsite.com</text>
  </svg>
  <h2 class="format-label format-label--facebook">Facebook Banner</h2>

  <!-- LinkedIn cover -->
  <svg class="banner banner--linkedin" viewBox="0 0 1049 319" aria-label="LinkedIn banner">
    <rect width="1049" height="319" fill="var(--paper)"/>
    <polygon points="881,0 1049,0 1049,269 754,269" fill="var(--cyan)"/>
    <polygon points="763,184 881,0 754,269 707,269" fill="var(--orange)"/>
    <polygon points="840,0 881,0 763,184" fill="var(--plum)"/>
    <rect y="269" width="1049" height="50" fill="var(--cyan)"/>
    <g class="brand-lockup">
      <text class="brand-name" x="515" y="152" font-size="64" text-anchor="middle">ovantri</text>
      <circle class="brand-dot" cx="645" cy="131" r="10"/>
    </g>
    <text class="join-label" x="335" y="299" font-size="15">JOIN US</text>
    <text class="handle" x="412" y="297" font-size="10" fill="var(--paper)">@companyaccount</text>
    <text class="website website--light" x="574" y="297" font-size="10">www.companywebsite.com</text>
  </svg>
  <h2 class="format-label format-label--linkedin">LinkedIn Banner</h2>

  <!-- Twitter header -->
  <svg class="banner banner--twitter" viewBox="0 0 1045 348" aria-label="Twitter banner">
    <rect width="1045" height="348" fill="var(--paper)"/>
    <polygon points="0,0 486,0 352,348 0,348" fill="var(--cyan)"/>
    <polygon points="486,0 495,0 398,348 352,348" fill="var(--mist)"/>
    <g class="brand-lockup">
      <text class="brand-name" x="723" y="162" font-size="64" text-anchor="middle">ovantri</text>
      <circle class="brand-dot" cx="853" cy="141" r="10"/>
    </g>
    <polygon class="join-bar" points="555,274 787,274 781,299 550,299"/>
    <text class="join-label" x="570" y="292" font-size="14">JOIN US</text>
    <text class="handle" x="645" y="290" font-size="9" fill="var(--sky)">@companyaccount</text>
    <text class="website" x="798" y="290" font-size="9">www.companywebsite.com</text>
  </svg>
  <h2 class="format-label format-label--twitter">Twitter Banner</h2>

  <!-- Instagram carousel -->
  <svg class="banner banner--post banner--post-1" viewBox="0 0 347 347" aria-label="Instagram post 1">
    <rect width="347" height="347" fill="var(--cyan)"/>
    <polygon points="85,40 347,40 347,306 185,306 162,347 0,347 0,193" fill="var(--paper)"/>
    <polygon class="join-bar" points="64,162 306,162 294,185 58,185"/>
    <text class="join-label" x="84" y="179" font-size="13">JOIN US</text>
    <text class="handle" x="156" y="178" font-size="9" fill="var(--sky)">@companyaccount</text>
  </svg>
  <svg class="banner banner--post banner--post-2" viewBox="0 0 347 347" aria-label="Instagram post 2">
    <rect width="347" height="347" fill="var(--paper)"/>
    <polygon points="0,0 232,0 210,40 0,40" fill="var(--cyan)"/>
    <rect y="306" width="347" height="41" fill="var(--cyan)"/>
    <g class="brand-lockup">
      <text class="brand-name" x="163" y="192" font-size="54" text-anchor="middle">ovantri</text>
      <circle class="brand-dot" cx="274" cy="174" r="9"/>
    </g>
    <text class="website website--light" x="173" y="331" font-size="11" text-anchor="middle">www.companywebsite.com</text>
  </svg>
  <svg class="banner banner--post banner--post-3" viewBox="0 0 347 347" aria-label="Instagram post 3">
    <rect width="347" height="347" fill="var(--paper)"/>
    <polygon points="221,0 347,0 347,347 0,347 0,306 131,306" fill="var(--cyan)"/>
    <polygon points="162,137 221,0 131,306 88,306" fill="var(--orange)"/>
    <polygon points="184,0 221,0 162,137" fill="var(--plum)"/>
  </svg>
  <h2 class="format-label format-label--instagram">Instagram Post</h2>

</body>
</html>
```